Investor Information Presentation Design Required and Corporate overview design

I have all the materials ready to go, just need 1x Pro Design for the presentation and 1x Pro Design for the corporate overview.
I am ok with images being changed (only if it represents the company better). Wording Can NOT be changed. Any process diagrams can be changed to better represent the process.
I can provide high res Logo file and obviously the files for the presentation and corporate overview. What I have done is basic, but need it to look far more polished and professional.

Target Market(s)

Fixed Term Deposits - $100,000 + High interest rates

Industry/Entity Type

Investment

Font styles to use
Sans Serif

Requirements
Must have
• A corporate professional look, think banks, financial services, business etc
• The presentation is NOT used for group presenting purposes - Individuals go through it on their own. Should want to make me feel like I have to read it all!

```html
<!DOCTYPE html>
<html lang="en">
<head>
<meta charset="utf-8">
<title>Norvale Capital – Investor Presentation</title>
<link href="https://fonts.googleapis.com/css2?family=Lato:wght@300;400;700&display=swap" rel="stylesheet">
<style>
:root{
  --navy:#323c52;
  --blue:#2f9fe0;
  --blue-light:#8ccaf0;
  --blue-pale:#e3f1fb;
  --canvas:#e2e2e2;
  --text-grey:#8a8f99;
  --white:#ffffff;
}
*{box-sizing:border-box;margin:0;padding:0}
html,body{width:1200px;height:1200px;overflow:hidden;background:var(--canvas);font-family:'Lato',sans-serif}
.board{display:grid;grid-template-columns:repeat(3,374px);grid-auto-rows:210px;column-gap:13px;row-gap:21px;padding:32px 26px}
.slide{position:relative;overflow:hidden;background:var(--white)}
.abs{position:absolute}
.brand{display:flex;flex-direction:column;align-items:center;gap:8px}
.brand-dot{width:44px;height:44px;border-radius:50%;background:var(--blue)}
.brand-name{font-weight:700;font-size:15px}
.cover{background:var(--navy);display:flex;align-items:center;justify-content:center}
.cover .brand-name{color:var(--white)}
.title-slide{display:flex;flex-direction:column;align-items:center;justify-content:center}
.title-slide .brand-dot{width:40px;height:40px}
.title-row{display:flex;align-items:center;gap:14px;margin-top:8px}
.title-row .rule{width:88px;height:2px;background:var(--blue)}
.title-row .brand-name{color:var(--navy);letter-spacing:1px;font-size:14px}
.subtitle{color:#333;font-size:15px;margin-top:6px}
.photo{position:absolute;inset:0}
.band{position:absolute;left:0;right:0;display:flex;align-items:center;justify-content:flex-end;padding-right:20px;color:var(--white);font-weight:300;font-size:21px}
.diamond{position:absolute;width:66px;height:66px;transform:rotate(45deg);background:var(--white);border:3px solid var(--blue);box-shadow:0 0 0 3px var(--white)}
.diamond svg{position:absolute;left:50%;top:50%;width:36px;height:36px;transform:translate(-50%,-50%) rotate(-45deg)}
.panel{position:absolute;top:0;bottom:0;background:var(--blue);color:var(--white);font-weight:300}
.panel ul{list-style:none}
.panel li{position:relative;padding-left:14px;font-size:12px;line-height:15px}
.panel li::before{content:"";position:absolute;left:0;top:4px;width:6px;height:6px;border:1px solid var(--white);border-radius:50%}
.notch-right::after{content:"";position:absolute;right:-14px;top:36px;border-left:14px solid var(--blue);border-top:13px solid transparent;border-bottom:13px solid transparent}
.notch-left::after{content:"";position:absolute;left:-14px;top:36px;border-right:14px solid var(--blue);border-top:13px solid transparent;border-bottom:13px solid transparent}
.heading{color:var(--blue);font-weight:300;text-align:center;line-height:1.15}
.bar{position:absolute;height:26px;background:var(--navy)}
.rates{position:absolute;left:9px;top:73px;width:231px;border-collapse:collapse;font-size:6px;text-align:center;color:#222}
.rates th{background:var(--blue-pale);font-weight:700;height:32px;border:1px solid var(--blue-light)}
.rates td{border:1px solid var(--blue-light);height:17px}
.rates tbody tr:nth-child(odd) td{background:var(--blue-pale)}
.notes{position:absolute;left:242px;top:72px;width:122px;font-size:5px;line-height:6.5px;color:var(--blue)}
.notes b{display:block;font-size:6px;margin-bottom:6px;letter-spacing:1px;font-weight:400}
.notes li{margin-left:10px;margin-bottom:3px}
.about-list{position:absolute;left:16px;top:60px;width:300px;list-style:none;color:var(--text-grey);font-size:10px;line-height:13px;font-weight:300}
.about-list li{position:relative;padding-left:14px}
.about-list li::before{content:"";position:absolute;left:0;top:3px;width:6px;height:6px;border:1px solid var(--text-grey);border-radius:50%}
.investors{background:var(--blue)}
.quote{position:absolute;background:rgba(90,100,115,.55);color:var(--white);font-size:4.6px;line-height:5.6px;font-style:italic;letter-spacing:.4px;padding:4px}
.team{position:absolute;top:48px;display:flex;flex-direction:column;align-items:center;text-align:center}
.avatar{width:48px;height:48px;border-radius:50%;background:#b9bcc2;border:2px solid var(--blue-light)}
.person{font-size:8px;color:#444;margin-top:7px}
.role{font-size:7px;color:var(--text-grey);margin-top:2px;line-height:8px}
.bio{list-style:none;text-align:left;font-size:4.5px;line-height:5.4px;color:var(--text-grey);margin-top:5px}
.social{position:absolute;bottom:7px;display:flex;gap:6px}
.social span{width:14px;height:14px;border-radius:50%;border:1.5px solid var(--blue)}
.contacts{position:absolute;left:6px;top:8px;width:176px;font-size:6px;line-height:7px;color:var(--text-grey)}
.contacts .lead{font-size:8.5px;line-height:10px;margin-bottom:10px}
.contacts h4{font-weight:400;color:#555;margin-top:8px}
.contacts .mail{color:var(--blue)}
.cta{position:absolute;left:114px;top:59px;width:66px;height:62px;border:1px solid var(--blue-light);color:var(--blue);font-size:8.5px;text-align:center;display:flex;align-items:center;justify-content:center;line-height:11px;background:var(--white)}
.closing{background:var(--navy)}
.closing-frame{position:absolute;left:68px;top:25px;width:229px;height:160px;border:1px solid #7c8496;display:flex;flex-direction:column;align-items:center;color:var(--white);text-align:center}
</style>
</head>
<body>
<main class="board">

  <section class="slide cover">
    <div class="brand"><span class="brand-dot"></span><span class="brand-name">Norvale Capital</span></div>
  </section>

  <section class="slide title-slide">
    <span class="brand-dot"></span>
    <div class="title-row"><span class="rule"></span><span class="brand-name">Norvale Capital</span><span class="rule"></span></div>
    <p class="subtitle">High Yield Term Deposits</p>
  </section>

  <section class="slide">
    <div class="photo" role="img" aria-label="Two businessmen reviewing a tablet in an office" style="background:linear-gradient(120deg,#f1f1f1 0%,#c9ced6 45%,#6e7686 100%)"></div>
    <div class="band" style="top:141px;height:48px;background:rgba(47,159,224,.8)">The Problem</div>
    <div class="diamond" style="left:52px;top:132px"><svg viewBox="0 0 36 36" fill="none" stroke="#323c52" stroke-width="2.5"><rect x="9" y="16" width="18" height="14" rx="2"/><path d="M12 16v-4a6 6 0 0 1 12 0v4"/><circle cx="18" cy="22" r="1.6" fill="#323c52"/></svg></div>
  </section>

  <section class="slide">
    <div class="panel notch-right" style="left:0;width:209px;padding:26px 14px 0 28px">
      <ul>
        <li style="margin-bottom:13px">Term deposits with leading banks pay less than 4.0% per annum</li>
        <li style="margin-bottom:13px">Savings are getting eroded by inflation</li>
        <li>Banks continue to profit despite paying low rates of return</li>
      </ul>
    </div>
    <svg class="abs" style="left:238px;top:46px" width="122" height="118" viewBox="0 0 122 118" fill="none" stroke="#2f9fe0" stroke-width="4" stroke-linejoin="round">
      <path d="M10 78 L78 12 Q92 22 112 14 L112 40 L48 104 Q30 92 10 100 Z"/>
      <circle cx="61" cy="58" r="15"/>
      <text x="61" y="65" font-family="Lato,sans-serif" font-size="20" font-weight="700" fill="#2f9fe0" stroke="none" text-anchor="middle">$</text>
    </svg>
  </section>

  <section class="slide">
    <div class="photo" role="img" aria-label="Business people standing behind a handshake" style="background:linear-gradient(180deg,#ffffff 0%,#dcdfe4 40%,#8a919e 100%)"></div>
    <div class="band" style="top:140px;height:50px;left:150px;background:rgba(140,202,240,.75);justify-content:center">The Solution</div>
    <div class="diamond" style="left:50px;top:128px"><svg viewBox="0 0 36 36" fill="none" stroke="#2f9fe0" stroke-width="2.5"><path d="M12 20a8 8 0 1 1 12 0c-1.5 1.5-2 3-2 5h-8c0-2-.5-3.5-2-5z"/><path d="M14 28h8M15 31h6"/></svg></div>
  </section>

  <section class="slide">
    <svg class="abs" style="left:16px;top:24px" width="150" height="150" viewBox="0 0 150 150" fill="none" stroke="#2f9fe0" stroke-width="4">
      <circle cx="50" cy="50" r="34" stroke-dasharray="10 6" stroke-width="10"/>
      <circle cx="50" cy="50" r="24"/><circle cx="50" cy="50" r="12"/>
      <circle cx="106" cy="106" r="28" stroke-dasharray="8 6" stroke-width="9"/>
      <circle cx="106" cy="106" r="19"/><circle cx="106" cy="106" r="9"/>
    </svg>
    <div class="panel notch-left" style="left:165px;right:0;padding:24px 12px 0 22px">
      <p style="font-size:12px;line-height:15px;margin-bottom:14px">Place your money with Norvale Capital to benefit from -</p>
      <ul>
        <li style="margin-bottom:15px">A fixed, high rate of return</li>
        <li style="margin-bottom:15px">Quarterly interest payments</li>
        <li style="margin-bottom:15px">Keeping ahead of inflation</li>
        <li>Access to other lucrative investment opportunities</li>
      </ul>
    </div>
  </section>

  <section class="slide">
    <div class="bar" style="left:0;width:104px;top:14px"></div>
    <div class="bar" style="right:0;width:104px;top:14px"></div>
    <h2 class="heading abs" style="left:104px;width:166px;top:14px;font-size:20px">Attractive Term Deposits</h2>
    <table class="rates">
      <thead><tr><th>Term</th><th>Investment Size</th><th>Effective Annual<br><br>Interest rate</th></tr></thead>
      <tbody>
        <tr><td>3 months</td><td>$100k-$5m</td><td>5.95%</td></tr>
        <tr><td>6 months</td><td>$100k-$5m</td><td>6.40%</td></tr>
        <tr><td>12 months</td><td>$100k-$5m</td><td>6.95%</td></tr>
        <tr><td>24 months</td><td>$100k-$5m</td><td>7.40%</td></tr>
      </tbody>
    </table>
    <div class="notes"><b>Note:</b>
      <ul>
        <li>Interest begins accruing from the day the funds arrive in the Norvale Capital bank account</li>
        <li>Each deposit is structured as a loan to Norvale Capital under the terms of the Deposit Agreement</li>
        <li>Interest is paid into your account each calendar quarter on 1 January, 1 April, 1 July and 1 October</li>
        <li>Deposit Agreements roll over for a further term unless notice is given no less than 14 days before the end of the term</li>
      </ul>
    </div>
  </section>

  <section class="slide">
    <div class="photo" role="img" aria-label="Business team shaking hands in a meeting" style="background:linear-gradient(120deg,#cfe3f2 0%,#7f94ad 50%,#3b4558 100%)"></div>
    <div class="band" style="top:142px;height:48px;background:rgba(50,60,82,.85);padding-right:40px">About Us</div>
    <div class="diamond" style="left:52px;top:131px"><svg viewBox="0 0 36 36" fill="none" stroke="#2f9fe0" stroke-width="2.5"><path d="M12 20a8 8 0 1 1 12 0c-1.5 1.5-2 3-2 5h-8c0-2-.5-3.5-2-5z"/><path d="M14 28h8M15 31h6"/></svg></div>
  </section>

  <section class="slide">
    <div class="bar" style="left:0;width:128px;top:21px"></div>
    <h2 class="heading abs" style="left:140px;top:21px;font-size:19px;white-space:nowrap">Who is Norvale Capital?</h2>
    <ul class="about-list">
      <li>Melbourne-based finance company (ACN: 000 111 222)</li>
      <li>Provides short term finance to qualified businesses</li>
      <li>Parent company (Brightline Holdings) established in 2009</li>
      <li>Norvale Capital brand launched late 2015</li>
      <li>Representation in Melbourne, Singapore, London,<br>New York &amp; Toronto</li>
      <li>Privy to unique high return investments due to<br>industry position</li>
      <li>Works alongside leading finance companies<br>with high quality, pre-vetted deal flow</li>
    </ul>
    <div class="abs" role="img" aria-label="Modern glass office tower" style="right:12px;top:110px;width:104px;height:90px;background:linear-gradient(160deg,#8fa6bf,#3f536b);clip-path:polygon(20% 100%,30% 20%,70% 0,80% 30%,100% 90%)"></div>
  </section>

  <section class="slide investors">
    <div class="abs" style="left:210px;right:0;top:20px;height:18px;background:#e8edf2"></div>
    <h2 class="abs" style="left:12px;top:21px;color:var(--white);font-weight:400;font-size:17px">Happy Investors Globally</h2>
    <div class="abs" role="img" aria-label="World map showing investor locations" style="left:10px;top:50px;width:355px;height:152px;background:radial-gradient(ellipse at 55% 45%,#7cc2ee 0%,#4fb0e8 60%,transparent 75%)"></div>
    <p class="quote" style="left:8px;top:52px;width:236px">"Well, I haven't found a good reason to say no. I was looking for a sound place for my savings and this offer was perfect for me, so I signed on with confidence." – P. Varga (Florida)<br>(Note: this investor placed a deposit after due diligence checks and added a further sum within 90 days.)</p>
    <p class="quote" style="left:282px;top:100px;width:72px">"I would like to reinvest all at the 24 month option plus invest an additional amount." – K. Morrow (Sydney, Australia)</p>
    <p class="quote" style="left:114px;top:152px;width:114px">"Great news, we would like to roll all of it over for 24 months and we will send another deposit." – T. Hale (Brisbane, Australia)</p>
  </section>

  <section class="slide">
    <div class="bar" style="left:0;width:98px;top:14px"></div>
    <div class="bar" style="right:0;width:98px;top:14px"></div>
    <h2 class="heading abs" style="left:98px;width:178px;top:6px;font-size:18px">Experienced Senior Management</h2>
    <div class="team" style="left:22px;width:100px"><span class="avatar"></span><p class="person">Daniel Archer</p><p class="role">Managing Director</p>
      <ul class="bio"><li>Former CEO of a listed firm</li><li>Broad investment experience</li><li>Bachelor of Laws and Commerce</li><li>Young leader award winner</li></ul></div>
    <div class="team" style="left:137px;width:100px"><span class="avatar"></span><p class="person">Rafiq Soomro</p><p class="role">Managing Partner</p>
      <ul class="bio"><li>Former business owner</li><li>Runs day-to-day operations</li><li>Digital strategy specialist</li><li>Engineering degree holder</li></ul></div>
    <div class="team" style="left:262px;width:100px"><span class="avatar"></span><p class="person">Tariq Halim</p><p class="role">Senior Account Manager</p>
      <ul class="bio"><li>10+ years in financial services</li><li>Former stockbroker</li><li>Works with investors</li></ul></div>
    <div class="social" style="left:32px"><span></span><span></span><span></span></div>
    <div class="social" style="left:155px"><span></span><span></span><span></span></div>
    <div class="social" style="left:279px"><span></span><span></span><span></span></div>
  </section>

  <section class="slide">
    <div class="bar" style="left:0;width:98px;top:14px"></div>
    <div class="bar" style="right:0;width:98px;top:14px"></div>
    <h2 class="heading abs" style="left:98px;width:178px;top:9px;font-size:18px">Experienced Senior Management</h2>
    <div class="team" style="left:6px;width:88px;top:56px"><span class="avatar"></span><p class="person">Daniel Archer</p><p class="role">Managing Director</p>
      <ul class="bio"><li>Regulated professional</li><li>Former stockbroker</li><li>Sources new opportunities</li></ul></div>
    <div class="team" style="left:100px;width:88px;top:52px"><span class="avatar"></span><p class="person">Graham Pellow</p><p class="role">Senior Advisor &amp; UK Representative</p>
      <ul class="bio"><li>Founder of a listed telecom</li><li>Management consulting</li><li>Provides vetted deals</li></ul></div>
    <div class="team" style="left:194px;width:88px;top:52px"><span class="avatar"></span><p class="person">Colin Ashby</p><p class="role">General Counsel</p>
      <ul class="bio"><li>20+ years in commercial law</li><li>Company secretary</li><li>Advises on compliance</li></ul></div>
    <div class="team" style="left:284px;width:88px;top:52px"><span class="avatar"></span><p class="person">Lena Hartanto</p><p class="role">Finance Manager</p>
      <ul class="bio"><li>Qualified accountant</li><li>Certified advisor</li><li>Manages group finances</li></ul></div>
    <div class="social" style="left:10px"><span></span><span></span><span></span></div>
    <div class="social" style="left:106px"><span></span><span></span><span></span></div>
    <div class="social" style="left:204px"><span></span><span></span><span></span></div>
    <div class="social" style="left:290px"><span></span><span></span><span></span></div>
  </section>

  <section class="slide">
    <div class="abs" role="img" aria-label="Smiling businesswoman holding a folder" style="left:189px;top:0;right:0;bottom:0;background:linear-gradient(135deg,#eef1f4 0%,#c8cdd5 55%,#8b8f98 100%)"></div>
    <div class="contacts">
      <p class="lead">To start earning a better rate of return on your money get started today!</p>
      <h4>Got Questions?</h4>
      <h4>Making an Investment (AU or US)</h4><p>Tariq Halim</p><p class="mail">clients@norvalecapital.example</p><p class="mail">+61 400 000 101</p>
      <h4>Customer Service Queries</h4><p>Rafiq Soomro</p><p class="mail">manager@norvalecapital.example</p><p class="mail">+61 (03) 9000 0100</p>
      <h4>Making an Investment (UK or Europe)</h4><p>Graham Pellow</p><p class="mail">clientsuk@norvalecapital.example</p><p class="mail">+44 70 0000 0200</p>
      <h4>Finance Queries</h4><p>Lena Hartanto</p><p class="mail">lena.h@brightlineholdings.example</p><p class="mail">+61 (03) 9000 0100</p>
    </div>
    <div class="cta">Click here to Download a Deposit Agreement</div>
    <div class="abs" style="left:189px;top:24px;width:134px;height:26px;background:var(--navy);color:var(--white);font-weight:300;font-size:18px;text-align:center;line-height:26px">Get Started</div>
  </section>

  <section class="slide closing">
    <div class="closing-frame">
      <span class="brand-dot" style="width:32px;height:32px;margin-top:14px"></span>
      <p style="font-weight:700;font-size:9px;margin-top:6px">Norvale Capital</p>
      <p style="font-weight:300;font-size:18px;margin-top:2px">Thank you</p>
      <p style="font-size:6.5px;line-height:9px;margin-top:14px">Norvale Capital Pty Ltd ACN: 000 111 222<br>Head Office: Suite 8.04 Harbourline Tower, 12<br>Quayside Dr, Southbank Melbourne 3000 VIC</p>
      <p style="font-size:6.5px;margin-top:12px">www.norvalecapital.example</p>
    </div>
  </section>

</main>
</body>
</html>
```